New Chiropractic Office needs a fresh flyer design!

We need a flyer design for our chiropractic office for our hometown based chiropractic office called "Corliss Chiropractic" Dr. Martin Corliss provides chiropractic services including adjustments, xrays and wellness exercises with a fresh approach to chiropractic which focuses on getting your body aligned correctly to be a better you. We dont like to focus on coming in just for pain although that is what most people associate our operation with so we understand that comes with the territory. However we would like our flyers to express health and wellness rather than medical or pain. We would like our flyer to emphasize our "New Patient Special" which includes consultation, exam, xrays and first treatment for only $50. We also accept most insurance plans. Call for an appointment 608-371-5829.

Industry/Entity Type

Office

```html
<!DOCTYPE html>
<html lang="en">
<head>
<meta charset="utf-8">
<title>Corliss Chiropractic – New Patient Special Flyer</title>
<link href="https://fonts.googleapis.com/css2?family=Tinos:ital,wght@0,400;0,700;1,700&family=Arimo:wght@400;700&display=swap" rel="stylesheet">
<style>
  :root {
    --stage: #e9ece6;
    --green-deep: #2f7d1c;
    --green-mid: #4aa22a;
    --green-bright: #8fd13c;
    --green-glow: #d8ee7a;
    --green-pale: #cfe8b8;
    --brown-line: #6b4a22;
    --ink: #111111;
    --sticker-cream: #fbe9a8;
    --sticker-edge: #ffffff;
    --price-red: #c8161d;
  }
  html, body {
    margin: 0;
    width: 1200px;
    height: 921px;
    overflow: hidden;
    background: var(--stage);
  }
  .flyer {
    position: absolute;
    left: 290px;
    top: 50px;
    width: 620px;
    height: 820px;
    overflow: hidden;
    background: radial-gradient(ellipse 60% 45% at 45% 58%, var(--green-glow) 0%, var(--green-bright) 35%, var(--green-mid) 65%, var(--green-deep) 100%);
    box-shadow: 0 6px 24px rgba(0,0,0,.18);
  }
  .flyer__curves {
    position: absolute;
    inset: 0;
  }
  .photo {
    position: absolute;
    inset: 0;
    background:
      radial-gradient(ellipse 28% 18% at 42% 30%, #e9b48f 0%, rgba(233,180,143,0) 100%),
      radial-gradient(ellipse 22% 16% at 78% 34%, #d9ae6a 0%, rgba(217,174,106,0) 100%),
      radial-gradient(ellipse 30% 10% at 50% 46%, #efc3a2 0%, rgba(239,195,162,0) 100%),
      linear-gradient(180deg, #ffffff 0%, #f7f4f1 60%, #fbfaf8 100%);
    clip-path: path('M0 0 H620 V452 Q300 300 0 318 Z');
  }
  .brand {
    position: absolute;
    left: 46px;
    top: 62px;
    margin: 0;
    font-family: 'Tinos', 'Times New Roman', serif;
    font-weight: 700;
    font-size: 21px;
    color: var(--green-deep);
  }
  .offer {
    position: absolute;
    left: 96px;
    top: 468px;
    font-family: 'Tinos', 'Times New Roman', serif;
    color: var(--ink);
  }
  .offer__title {
    margin: 0;
    font-size: 23px;
    font-weight: 400;
    white-space: nowrap;
  }
  .offer__title strong { font-weight: 700; }
  .offer__list {
    list-style: none;
    margin: 0;
    padding: 0;
    font-style: italic;
    font-weight: 700;
    font-size: 17px;
  }
  .offer__list li { position: absolute; white-space: nowrap; }
  .offer__list li::before { content: "\2022\00a0"; font-style: normal; }
  .offer__list li:nth-child(1) { left: 8px;  top: 44px; }
  .offer__list li:nth-child(2) { left: 20px; top: 83px; }
  .offer__list li:nth-child(3) { left: 30px; top: 124px; }
  .offer__list li:nth-child(4) { left: 40px; top: 166px; }
  .price-sticker {
    position: absolute;
    left: 410px;
    top: 546px;
    width: 160px;
    height: 160px;
  }
  .price-sticker__text {
    position: absolute;
    left: 0;
    top: 44px;
    width: 150px;
    text-align: center;
    font-family: 'Tinos', 'Times New Roman', serif;
    line-height: 1;
  }
  .price-sticker__lead { display: block; font-size: 21px; color: var(--price-red); }
  .price-sticker__amount { display: block; font-size: 46px; font-weight: 700; color: var(--price-red); margin-top: 2px; }
  .contact-band {
    position: absolute;
    left: 0;
    right: 0;
    top: 714px;
    height: 82px;
    background: linear-gradient(180deg, rgba(255,255,255,.75), var(--green-pale));
    font-family: 'Arimo', Arial, sans-serif;
    color: var(--ink);
  }
  .contact-band p { margin: 0; position: absolute; left: 0; right: 0; text-align: center; white-space: nowrap; }
  .contact-band__insurance { top: 8px; font-size: 17px; }
  .contact-band__call { top: 38px; font-size: 18px; }
  .contact-band__phone { font-weight: 700; font-size: 21px; margin-left: 4px; }
  .flyer__foot {
    position: absolute;
    left: 0; right: 0; bottom: 0;
    height: 24px;
    background: linear-gradient(90deg, var(--green-mid), var(--green-bright));
  }
</style>
</head>
<body>
  <article class="flyer">
    <svg class="flyer__curves" width="620" height="820" viewBox="0 0 620 820" aria-hidden="true">
      <defs>
        <linearGradient id="swoosh" x1="0" y1="0" x2="1" y2="0">
          <stop offset="0" stop-color="#3d9a1f"/>
          <stop offset=".5" stop-color="#8fd13c"/>
          <stop offset="1" stop-color="#3d9a1f"/>
        </linearGradient>
      </defs>
      <path d="M0 318 Q300 300 620 452 V500 Q300 360 0 360 Z" fill="url(#swoosh)"/>
      <path d="M0 360 Q300 360 620 500 V508 Q300 372 0 369 Z" fill="var(--brown-line)" opacity=".75"/>
    </svg>

    <div class="photo" role="img" aria-label="Photo of a relaxed woman lying face down on a white table receiving a back massage, a pale hibiscus flower beside her arm"></div>

    <p class="brand">Corliss Chiropractic</p>

    <section class="offer">
      <h1 class="offer__title"><strong>New Patient Special</strong> which includes:</h1>
      <ul class="offer__list">
        <li>Consultation</li>
        <li>Exam</li>
        <li>X-Rays</li>
        <li>First Treatment</li>
      </ul>
    </section>

    <div class="price-sticker">
      <svg width="160" height="160" viewBox="0 0 160 160" aria-hidden="true">
        <circle cx="75" cy="78" r="74" fill="var(--sticker-edge)"/>
        <circle cx="75" cy="78" r="67" fill="var(--sticker-cream)"/>
        <path d="M112 12 Q150 30 150 70 Q128 48 112 12 Z" fill="#ffffff" stroke="#d9d9d9" stroke-width="1"/>
      </svg>
      <div class="price-sticker__text">
        <span class="price-sticker__lead">for only</span>
        <span class="price-sticker__amount">$50</span>
      </div>
    </div>

    <footer class="contact-band">
      <p class="contact-band__insurance">We also accept most insurance plans</p>
      <p class="contact-band__call">Call for an appointment <span class="contact-band__phone">608-371-5829</span></p>
    </footer>
    <div class="flyer__foot"></div>
  </article>
</body>
</html>
```